Stationary, memo and report templates for professional services company

Looking for someone to update stationary design but just as importantly come up with a template for reports and memos for use in our consulting firm. Would also like some brand use guidelines to be able to share with our whole team. We have an existing logo that we like. Need to update with a more contemporary look so that our deliverables to clients look good and professional yet stylish. This is for business to business communications. No need for envelope design. Important to have design for multiple pages, i.e. first page of a report and then 2nd page. Need to use in MS word documents so must be easy to use and replicate. Don't want something overly complex. Clean, fresh looking is best.

Target Market(s)

Business to business; non-profit cultural attractions

Colors

Designer to choose colors to be used in the design.

Requirements
Must have
• Clean look but with a little style or pop. Something that can easily be used in word documents. Need to have page styles that have a first page of a report (not a cover page) and then secondary page.
Nice to have
• Although the dark blue is our primary color. Might be willing to look at some accent color as well.
Should not have
• Not just our logo on the page with a color bar.

```html
<!DOCTYPE html>
<html lang="en">
<head>
<meta charset="utf-8">
<title>Parkline Advisors – Report Pages</title>
<link href="https://fonts.googleapis.com/css2?family=Montserrat:wght@400;600&display=swap" rel="stylesheet">
<style>
  :root{
    --navy:#13287a;
    --navy-deep:#0c1d63;
    --ink:#2a2a2a;
    --rule:#c9c9cc;
    --stage-a:#5a5a5a;
    --stage-b:#2b2b2b;
    --paper:#ffffff;
    --paper-end:#e9e9eb;
  }
  *{box-sizing:border-box;margin:0;padding:0}
  html,body{width:1200px;height:1200px;overflow:hidden}
  body{
    background:radial-gradient(ellipse at 55% 30%,var(--stage-a) 0%,var(--stage-b) 75%);
    font-family:"Montserrat",sans-serif;
    position:relative;
  }
  .page{
    position:absolute;width:579px;height:818px;
    background:linear-gradient(180deg,var(--paper) 0%,var(--paper) 70%,var(--paper-end) 100%);
    box-shadow:0 4px 10px rgba(0,0,0,.45);
    overflow:hidden;
  }
  .page--first{left:20px;top:16px}
  .page--second{left:610px;top:368px}
  .header-swoosh{position:absolute;left:0;top:0;width:579px;height:140px}
  .brand-name{
    position:absolute;left:24px;top:30px;
    color:#fff;font-weight:600;font-size:17px;letter-spacing:.5px;line-height:1.15;
  }
  .brand-name--footer{color:var(--navy);top:auto;bottom:30px;font-size:15px}
  .body{
    position:absolute;left:23px;width:532px;
    color:var(--ink);font-size:10.2px;line-height:12.8px;text-align:justify;
  }
  .page--first .body{top:142px}
  .page--second .body{top:30px}
  .body p{margin-bottom:12.8px}
  .body h2{
    color:var(--navy);font-weight:600;font-size:17px;line-height:20px;
    margin:27px 0 14px;text-align:left;
  }
  .body strong{font-weight:600;color:#111}
  .web{
    position:absolute;left:0;right:0;bottom:24px;text-align:center;
    font-size:11.5px;letter-spacing:.8px;color:#333;
  }
  .page--second .web{left:222px;right:auto;bottom:23px}
  .footer-rule{position:absolute;left:0;right:0;bottom:8px;height:3px;background:var(--rule)}
  .footer-band{position:absolute;left:0;right:0;bottom:0;height:8px;background:var(--navy)}
</style>
</head>
<body>

<section class="page page--first">
  <svg class="header-swoosh" viewBox="0 0 579 140" preserveAspectRatio="none" aria-hidden="true">
    <defs>
      <linearGradient id="blueFill" x1="0" y1="0" x2="1" y2="1">
        <stop offset="0" stop-color="#0c1d63"/><stop offset="1" stop-color="#1d3fa0"/>
      </linearGradient>
      <linearGradient id="greyFill" x1="0" y1="0" x2="1" y2="0">
        <stop offset="0" stop-color="#8a8a8a"/><stop offset="1" stop-color="#3a3a3a"/>
      </linearGradient>
    </defs>
    <path d="M0 0 H400 C300 20 230 70 150 100 C95 120 45 126 0 122 Z" fill="url(#blueFill)"/>
    <path d="M0 112 C60 116 130 102 190 76 C260 45 330 10 400 0 H420 C340 14 270 50 200 84 C130 114 60 122 0 118 Z" fill="#3f63c4" opacity=".5"/>
    <path d="M360 0 H579 V52 C540 22 480 6 400 4 Z" fill="url(#greyFill)"/>
  </svg>
  <div class="brand-name">PARKLINE<br>ADVISORS</div>

  <div class="body">
    <p>Parkline Advisors is a full-service consulting firm providing business, organizational, analytical, fundraising, and financial expertise to zoo, animal, and conservation organizations. We have many years of experience working with zoological institutions across the country. Martin Hale, PA’s Principal, is well respected within the industry and has earned accolades from his clients and peers. He works collaboratively with design teams to provide realistic, yet visionary ideas for growth for facilities, organizations, and funding.</p>
    <p>Parkline Advisors’ philosophy is to balance your conservation and education mission with its bottom line and the need for financial sustainability. We understand the challenge of balancing the client’s institutional vision while maximizing your funding and managing the organization and expenses. We have helped many of your colleagues create high performing organizations and can leverage that expertise for you.</p>
    <p>Our team has extensive experience in working with zoos of all sizes across the country. We have helped develop Strategic, Business, and Operational Plans for more than fifty ACWA-accredited institutions with budgets from less than $1,000,000 to over $30,000,000 and attendance ranging from 75,000 to over 2,500,000. We regularly provide expert counsel to zoo leaders across the country. One of the key advantages Parkline Advisors provides is its ability to unite stakeholders behind a common vision and develop an actionable plan to achieve success.</p>
    <h2>Our Philosophy</h2>
    <p>We know you have a choice of consulting services, but we’re confident you’ll appreciate the Parkline Advisors difference.</p>
    <p><strong>We listen to you and we respond.</strong> We’ll spend time with you before you hire us to make sure we get it right from the start and we’ll be there for you whenever you need us.</p>
    <p><strong>We work to help secure your long-term success.</strong> With each project, we provide a three- to six-month follow-up check to make sure you’re on track.</p>
    <p><strong>We nurture lasting relationships.</strong> We guarantee your satisfaction and will do whatever it takes to make sure you’re pleased with our services.</p>
    <p><strong>We believe that your mission comes first.</strong> To support the important work of our clients, we’re committed to giving back and contributing to ACWA’s Conservation Endowment Fund for each of our consulting engagements.</p>
    <p>Lorem ipsum dolor sit amet, consectetuer adipiscing elit, sed diam nonummy nibh euismod tincidunt ut laoreet dolore magna aliquam erat volutpat. Ut wisi enim ad minim veniam, quis nostrud exerci tation ullamcorper suscipit lobortis nisl ut aliquip ex ea commodo consequat. Duis autem vel eum iriure dolor in hendrerit in vulputate velit esse molestie consequat, vel illum dolore eu feugiat nulla facilisis at vero eros et accumsan et iusto odio dignissim qui blandit praesent luptatum zzril delenit augue duis dolore te feugait nulla facilisi. Lorem ipsum dolor sit amet, consectetuer adipiscing elit, sed diam nonummy nibh euismod tincidunt ut laoreet dolore magna aliquam erat volutpat. Ut wisi enim ad minim veniam, quis nostrud exerci tation ullamcorper suscipit lobortis nisl ut aliquip ex ea commodo consequat.</p>
  </div>

  <div class="web">www.parklineadvisors.com</div>
  <div class="footer-rule"></div>
  <div class="footer-band"></div>
</section>

<section class="page page--second">
  <div class="body">
    <p>Parkline Advisors is a full-service consulting firm providing business, organizational, analytical, fundraising, and financial expertise to zoo, animal, and conservation organizations. We have many years of experience working with zoological institutions across the country. Martin Hale, PA’s Principal, is well respected within the industry and has earned accolades from his clients and peers. He works collaboratively with design teams to provide realistic, yet visionary ideas for growth for facilities, organizations, and funding.</p>
    <p>Parkline Advisors’ philosophy is to balance your conservation and education mission with its bottom line and the need for financial sustainability. We understand the challenge of balancing the client’s institutional vision while maximizing your funding and managing the organization and expenses. We have helped many of your colleagues create high performing organizations and can leverage that expertise for you.</p>
    <p>Our team has extensive experience in working with zoos of all sizes across the country. We have helped develop Strategic, Business, and Operational Plans for more than fifty ACWA-accredited institutions with budgets from less than $1,000,000 to over $30,000,000 and attendance ranging from 75,000 to over 2,500,000. We regularly provide expert counsel to zoo leaders across the country. One of the key advantages Parkline Advisors provides is its ability to unite stakeholders behind a common vision and develop an actionable plan to achieve success.</p>
    <h2>Our Philosophy</h2>
    <p>We know you have a choice of consulting services, but we’re confident you’ll appreciate the Parkline Advisors difference.</p>
    <p><strong>We listen to you and we respond.</strong> We’ll spend time with you before you hire us to make sure we get it right from the start and we’ll be there for you whenever you need us.</p>
    <p><strong>We work to help secure your long-term success.</strong> With each project, we provide a three- to six-month follow-up check to make sure you’re on track.</p>
    <p><strong>We nurture lasting relationships.</strong> We guarantee your satisfaction and will do whatever it takes to make sure you’re pleased with our services.</p>
    <p><strong>We believe that your mission comes first.</strong> To support the important work of our clients, we’re committed to giving back and contributing to ACWA’s Conservation Endowment Fund for each of our consulting engagements.</p>
    <p>Lorem ipsum dolor sit amet, consectetuer adipiscing elit, sed diam nonummy nibh euismod tincidunt ut laoreet dolore magna aliquam erat volutpat. Ut wisi enim ad minim veniam, quis nostrud exerci tation ullamcorper suscipit lobortis nisl ut aliquip ex ea commodo consequat. Duis autem vel eum iriure dolor in hendrerit in vulputate velit esse molestie consequat, vel illum dolore eu feugiat nulla facilisis at vero eros et accumsan et iusto odio dignissim qui blandit praesent luptatum zzril delenit augue duis dolore te feugait nulla facilisi. Lorem ipsum dolor sit amet, consectetuer adipiscing elit, sed diam nonummy nibh euismod tincidunt ut laoreet dolore magna aliquam erat volutpat. Ut wisi enim ad minim veniam, quis nostrud exerci tation ullamcorper suscipit lobortis nisl ut aliquip ex ea commodo consequat.</p>
  </div>

  <div class="brand-name brand-name--footer">PARKLINE<br>ADVISORS</div>
  <div class="web">www.parklineadvisors.com</div>
  <div class="footer-rule"></div>
  <div class="footer-band"></div>
</section>

</body>
</html>
```